Weigh Fresh Dwelling Business card

I have had at the logo designed here and attached. The business compares off the plan apartments in Sydney and provides quick comparison for new home buyers e.g price, floor plans and location. I would like the complimentary colours used on the business card. I would like it be unique but also look professional. I also have a website to gain inspiration from www.weighfreshdwelling.com.au
Updates
Industry/Entity Type
Business
Contact Information for Business Card
Lena Vortigan
Director of Business Development
e: lena.vortigan@weighfreshdwelling.com.au
p: (02) 7394 6628
m: 0431 572 908
w: www.weighfreshdwelling.com.au
Look and feel
Each slider illustrates characteristics of the customer's brand and the style your logo design should communicate.

```html
<!DOCTYPE html>
<html lang="en">
<head>
<meta charset="utf-8">
<title>Weigh Fresh Dwelling Business Card</title>
<link rel="stylesheet" href="https://fonts.googleapis.com/css2?family=Source+Sans+3:wght@400;600;700&display=swap">
<style>
  :root {
    --backdrop: #e9ecef;
    --card: #ffffff;
    --brand-green: #84c33b;
    --brand-blue: #229ee0;
    --text-light: #ffffff;
  }
  html, body {
    margin: 0;
    width: 1200px;
    height: 900px;
    overflow: hidden;
    background: var(--backdrop);
    font-family: "Source Sans 3", "Myriad Pro", Arial, sans-serif;
  }
  .business-card {
    position: absolute;
    left: 100px;
    top: 141px;
    width: 1000px;
    height: 618px;
    background: var(--card);
    box-shadow: 0 10px 30px rgba(0,0,0,0.18);
    overflow: hidden;
  }
  .field-art {
    position: absolute;
    inset: 0;
    width: 100%;
    height: 100%;
  }
  .brand-mark {
    position: absolute;
    left: 232px;
    top: 112px;
    width: 96px;
    height: 96px;
    background: var(--brand-blue);
  }
  .brand-name {
    position: absolute;
    left: 88px;
    top: 232px;
    margin: 0;
    font-size: 44px;
    font-weight: 400;
    line-height: 1;
    color: var(--brand-green);
    white-space: nowrap;
  }
  .contact-block {
    position: absolute;
    right: 24px;
    margin: 0;
    text-align: right;
    color: var(--text-light);
    white-space: nowrap;
  }
  .person-name {
    top: 270px;
    font-size: 33px;
    font-weight: 700;
    line-height: 1.1;
  }
  .person-title {
    top: 310px;
    font-size: 26px;
    font-weight: 400;
    line-height: 1.2;
  }
  .postal-address {
    top: 362px;
    font-size: 26px;
    line-height: 35px;
    font-style: normal;
  }
  .contact-list {
    position: absolute;
    right: 24px;
    top: 456px;
    margin: 0;
    padding: 0;
    list-style: none;
    color: var(--text-light);
    font-size: 26px;
    line-height: 36px;
    white-space: nowrap;
  }
  .contact-list li {
    display: flex;
    justify-content: flex-end;
    align-items: center;
    gap: 14px;
  }
  .contact-icon {
    width: 18px;
    height: 18px;
    flex: none;
  }
</style>
</head>
<body>
  <article class="business-card">
    <svg class="field-art" viewBox="0 0 1000 618" preserveAspectRatio="none" aria-hidden="true">
      <path fill="var(--brand-green)" d="M0,430 C200,520 380,520 520,400 C640,300 800,190 1000,200 L1000,618 L0,618 Z"/>
      <rect x="0" y="606" width="1000" height="12" fill="var(--brand-blue)"/>
    </svg>

    <div class="brand-mark" aria-hidden="true"></div>
    <h1 class="brand-name">Weigh Fresh Dwelling</h1>

    <h2 class="contact-block person-name">Oliver Pembrook</h2>
    <p class="contact-block person-title">Managing Director</p>
    <address class="contact-block postal-address">48 Harbour Lane, Sydney NSW 2000<br>Australia</address>

    <ul class="contact-list">
      <li>(02) 7394 6628
        <svg class="contact-icon" viewBox="0 0 24 24" aria-hidden="true"><path fill="#fff" d="M6.6 10.8a15 15 0 0 0 6.6 6.6l2.2-2.2a1 1 0 0 1 1-.25 11.4 11.4 0 0 0 3.6.57 1 1 0 0 1 1 1V20a1 1 0 0 1-1 1A17 17 0 0 1 3 4a1 1 0 0 1 1-1h3.5a1 1 0 0 1 1 1c0 1.25.2 2.45.57 3.57a1 1 0 0 1-.25 1z"/></svg>
      </li>
      <li>info@weighfreshdwelling.com.au
        <svg class="contact-icon" viewBox="0 0 24 24" aria-hidden="true"><rect x="3" y="6" width="18" height="12" fill="#fff"/><path d="M3 6l9 7 9-7" fill="none" stroke="var(--brand-green)" stroke-width="1.6"/></svg>
      </li>
      <li>www.weighfreshdwelling.com.au
        <svg class="contact-icon" viewBox="0 0 24 24" aria-hidden="true"><circle cx="12" cy="12" r="9" fill="#fff"/><path d="M3 12h18M12 3c3 3 3 15 0 18M12 3c-3 3-3 15 0 18" fill="none" stroke="var(--brand-green)" stroke-width="1.4"/></svg>
      </li>
    </ul>
  </article>
</body>
</html>
```